Business Card Revision

Need to redesign my business cards for a new professional look. We are a courier company. You can go to www.qvroutefast.com to see what we do. The trucks have an old company name (Nimble) on them but that is the company we are just now
changing the name.

Target Market(s)

Potential clients. We service the automotive, plumbing, printing, air freight industries as well as many others.

Industry/Entity Type

Business

Contact Information for Business Card

QVrushline
20583 Palmer Fenwick Parkway
Cincinnati, Oh 45317

Howard T. Lassiter
President

howie@qvroutefast.com

Main: (513) 555-0147

```html
<!DOCTYPE html>
<html lang="en">
<head>
<meta charset="utf-8">
<title>QV Routefast Business Card</title>
<link href="https://fonts.googleapis.com/css2?family=Open+Sans:wght@400;700;800&display=swap" rel="stylesheet">
<style>
  :root {
    --stage: #dcdce0;
    --brand-blue: #1f74b4;
    --brand-blue-dark: #135f9c;
    --brand-blue-light: #2a8bc4;
    --ink: #222428;
    --paper: #ffffff;
  }
  * { margin: 0; padding: 0; box-sizing: border-box; }
  html, body {
    width: 1200px;
    height: 720px;
    overflow: hidden;
    background: var(--stage);
    font-family: "Open Sans", Arial, sans-serif;
  }
  .canvas {
    position: relative;
    width: 1200px;
    height: 720px;
  }
  .card {
    position: absolute;
    top: 223px;
    width: 465px;
    height: 266px;
  }
  .card-front {
    left: 104px;
    background: linear-gradient(135deg, var(--brand-blue-dark) 0%, var(--brand-blue) 50%, var(--brand-blue-light) 100%);
  }
  .card-back {
    left: 630px;
    background: var(--paper);
  }
  .wordmark {
    position: absolute;
    font-weight: 800;
    letter-spacing: 1px;
    white-space: nowrap;
  }
  .card-front .wordmark {
    left: 0;
    right: 0;
    top: 112px;
    text-align: center;
    font-size: 32px;
    color: var(--paper);
  }
  .card-back .wordmark {
    left: 36px;
    top: 112px;
    font-size: 25px;
    line-height: 1.05;
    color: var(--brand-blue);
  }
  .contact {
    position: absolute;
    left: 259px;
    top: 82px;
    color: var(--ink);
    font-size: 12px;
    line-height: 14px;
  }
  .contact-name {
    color: var(--brand-blue);
    font-weight: 700;
    font-size: 14px;
    line-height: 16px;
    text-transform: uppercase;
    letter-spacing: 0.2px;
  }
  .contact-title { margin-bottom: 14px; }
  .contact-address { margin-bottom: 8px; }
  .contact-line {
    display: flex;
    align-items: center;
    gap: 5px;
    margin-bottom: 3px;
  }
  .contact-line svg { flex: none; }
</style>
</head>
<body>
<main class="canvas">
  <section class="card card-front">
    <div class="wordmark">QV ROUTEFAST</div>
  </section>

  <section class="card card-back">
    <div class="wordmark">QV<br>ROUTEFAST</div>
    <div class="contact">
      <p class="contact-name">Howard T. Lassiter</p>
      <p class="contact-title">President</p>
      <p class="contact-address">20583 Palmer Fenwick Parkway<br>Cincinnati, Oh 45317</p>
      <p class="contact-line">
        <svg width="11" height="9" viewBox="0 0 11 9" aria-hidden="true">
          <path d="M0.5 3 Q5.5 -0.5 10.5 3 L9 4.2 L7.4 3.4 L7.4 2.4 Q5.5 1.8 3.6 2.4 L3.6 3.4 L2 4.2 Z" fill="#1f74b4"/>
          <rect x="2.5" y="4.5" width="6" height="4" rx="0.8" fill="#1f74b4"/>
        </svg>
        (513) 555-0147
      </p>
      <p class="contact-line">
        <svg width="11" height="8" viewBox="0 0 11 8" aria-hidden="true">
          <rect x="0" y="0" width="11" height="8" rx="0.8" fill="#1f74b4"/>
          <path d="M0.6 0.8 L5.5 4.6 L10.4 0.8" fill="none" stroke="#ffffff" stroke-width="1"/>
        </svg>
        howie@qvroutefast.com
      </p>
    </div>
  </section>
</main>
</body>
</html>
```